Corvello Paintless Dent Removal

Our company works on vehicles removing dents using a highly skilled trade which the metal is massaged out with special tools without disturbing the original paint, hence paintless dent removal. Besides keeping the paint and metal original its also very environmentally friendly since no paint or toxic fillers are used. Also we we are one of the most experienced companies in the business with 25 years

Target Market(s)

Retail Automobile consumers, Auto Dealerships and Auto Body Shops

Industry/Entity Type

Auto Repair

Contact Information for Business Card

Dwight Halvorsen
PO Box 538 Ashbrook, NY 11892
631-472-8169
corvellopdr@mailnest.example
website corvellopdr.example
youtube corvello paintless dent removal
25 years of experience removing Dents, Dings and Hail Damage

Font styles to use
Serif
Sans Serif

Colors

Designer to choose colors to be used in the design.

Requirements
Must have
• I do like things that are simple but classy and somewhat bold, also I like my logo so that should be somewhat important

```html
<!DOCTYPE html>
<html lang="en">
<head>
<meta charset="utf-8">
<title>Corvello Paintless Dent Removal – Business Card</title>
<link rel="stylesheet" href="https://fonts.googleapis.com/css2?family=Noto+Sans:ital,wght@0,400;0,700;1,400&display=swap">
<style>
  :root {
    --backdrop: #c7b099;
    --paper: #ffffff;
    --navy: #112a52;
    --lime: #7cc52a;
    --ink: #3a3a3a;
    --muted: #666666;
  }
  * { margin: 0; padding: 0; box-sizing: border-box; }
  html, body {
    width: 1200px; height: 1200px; overflow: hidden;
    background: var(--backdrop);
    font-family: "Noto Sans", Tahoma, sans-serif;
  }
  .sheet {
    position: relative; width: 1200px; height: 1200px;
    display: flex; flex-direction: column; align-items: center; justify-content: center; gap: 80px;
  }
  .card {
    position: relative; width: 700px; height: 400px;
    background: var(--paper);
    box-shadow: 0 12px 30px rgba(60, 40, 20, 0.25);
    overflow: hidden;
  }
  .card-bands { position: absolute; inset: 0; width: 700px; height: 400px; }

  /* front */
  .brand { position: absolute; left: 44px; top: 40px; color: var(--navy); font-weight: 700; line-height: 1; }
  .brand-name { font-size: 38px; letter-spacing: -0.5px; }
  .brand-sub { font-size: 14px; margin-top: 2px; }
  .holder { position: absolute; left: 44px; top: 120px; }
  .holder-name { font-size: 20px; font-weight: 700; color: var(--navy); letter-spacing: 0.3px; }
  .holder-role { font-size: 14px; color: var(--ink); font-weight: 700; }
  .contact {
    position: absolute; right: 44px; top: 170px; text-align: right;
    font-size: 18px; line-height: 1.3; color: var(--ink); list-style: none;
  }
  .social { position: absolute; right: 44px; top: 318px; display: flex; gap: 8px; list-style: none; }
  .social li { width: 16px; height: 16px; border-radius: 50%; background: var(--lime); border: 2px solid var(--navy); }

  /* back */
  .brand-centre {
    position: absolute; left: 0; right: 0; top: 130px; text-align: center; color: var(--navy); font-weight: 700;
  }
  .brand-centre .brand-name { font-size: 58px; line-height: 1; display: inline-flex; align-items: center; gap: 14px; }
  .brand-centre .brand-mark { width: 22px; height: 22px; border-radius: 50%; background: var(--lime); }
  .brand-centre .brand-sub { font-size: 22px; margin-top: 6px; }
  .tagline {
    position: absolute; left: 0; right: 0; top: 262px; text-align: center;
    font-size: 13px; font-style: italic; color: var(--muted);
  }
</style>
</head>
<body>
<main class="sheet">

  <section class="card card-front" aria-label="Business card front">
    <svg class="card-bands" viewBox="0 0 700 400" aria-hidden="true">
      <rect x="0" y="384" width="700" height="16" fill="var(--lime)"/>
      <path d="M96 400 V386 Q96 372 112 372 H700 V400 Z" fill="var(--navy)"/>
    </svg>
    <div class="brand">
      <div class="brand-name">CORVELLO</div>
      <div class="brand-sub">Paintless Dent Removal</div>
    </div>
    <div class="holder">
      <div class="holder-name">DWIGHT HALVORSEN</div>
      <div class="holder-role">Designation</div>
    </div>
    <ul class="contact">
      <li>631-472-8169</li>
      <li>corvellopdr@mailnest.example</li>
      <li>corvellopdr.example</li>
      <li>PO Box 538 Ashbrook, NY 11892</li>
      <li>corvello paintless dent removal</li>
    </ul>
    <ul class="social" aria-label="Social links">
      <li></li><li></li><li></li><li></li><li></li>
    </ul>
  </section>

  <section class="card card-back" aria-label="Business card back">
    <svg class="card-bands" viewBox="0 0 700 400" aria-hidden="true">
      <path d="M0 0 H700 V14 Q700 26 684 26 H0 Z" fill="var(--navy)"/>
      <path d="M0 378 H650 Q666 378 670 400 H0 Z" fill="var(--lime)"/>
    </svg>
    <div class="brand-centre">
      <div class="brand-name"><span class="brand-mark"></span>CORVELLO</div>
      <div class="brand-sub">Paintless Dent Removal</div>
    </div>
    <p class="tagline">25 years of experience removing Dents, Dings and Hail Damage</p>
  </section>

</main>
</body>
</html>
```